Norvane Builders Business Card

Modern and Professional Business Card for a Med size construction/development company.

See the samples below for the design I like … but I need ideas for incorporating the red company logo while still keeping the clean look of the card samples that are attached.

Logo and tag line on the back … info on the front.

Tagline: Built Solid From Every Foundation

Target Market(s)

Med-Large General Contractors

Contact Information for Business Card

Norvane Builders Limited
42 Brenton Street
Elk Harbour, NL
B3K 7T2

t: 709-555-0147
f: 709-555-0192
w: www.norvanebuilders-example.com

Font styles to use
Sans Serif

Colors
fbee3e

Requirements
Must have
• I like the black and yellow designs of the attached samples …. but I'm not sure how to incorporate the red Norvane Builders logo into that design??
Nice to have
• Construction safety strips

```html
<!DOCTYPE html>
<html lang="en">
<head>
<meta charset="utf-8">
<title>Norvane Builders Business Card</title>
<link href="https://fonts.googleapis.com/css2?family=Roboto:wght@400;500;700;900&display=swap" rel="stylesheet">
<style>
  :root {
    --page-bg: #ededed;
    --brand-red: #e0332e;
    --card-dark: #262626;
    --ink-light: #ffffff;
    --logo-ink: #1a1a1a;
  }
  * { margin: 0; padding: 0; box-sizing: border-box; }
  html, body {
    width: 1124px;
    height: 1200px;
    overflow: hidden;
    background: var(--page-bg);
    font-family: "Roboto", Arial, sans-serif;
  }
  .card {
    position: absolute;
    left: 212px;
    box-shadow: 0 2px 6px rgba(0,0,0,0.25);
    overflow: hidden;
  }
  .card--front {
    top: 174px;
    width: 708px;
    height: 406px;
    background: var(--card-dark);
  }
  .card--back {
    top: 627px;
    width: 710px;
    height: 412px;
    background: var(--brand-red);
  }
  .front-wedge {
    position: absolute;
    left: 0; top: 0;
    width: 708px; height: 406px;
  }
  .wordmark {
    position: absolute;
    transform: translate(-50%, -50%);
    text-align: center;
    color: var(--logo-ink);
    font-weight: 900;
    text-transform: uppercase;
    line-height: 1;
    white-space: nowrap;
  }
  .wordmark__main { display: block; }
  .wordmark__sub { display: block; }
  .card--front .wordmark { left: 192px; top: 209px; }
  .card--front .wordmark__main { font-size: 52px; letter-spacing: -0.5px; }
  .card--front .wordmark__sub { font-size: 21px; margin-top: 36px; letter-spacing: 1px; }
  .card--back .wordmark { left: 355px; top: 212px; }
  .card--back .wordmark__main { font-size: 74px; letter-spacing: -0.5px; }
  .card--back .wordmark__sub { font-size: 30px; margin-top: 48px; letter-spacing: 1.5px; }

  .contact__company {
    position: absolute;
    left: 379px;
    top: 106px;
    color: var(--brand-red);
    font-size: 23px;
    font-weight: 400;
    white-space: nowrap;
  }
  .contact__row {
    position: absolute;
    left: 381px;
    display: flex;
    align-items: flex-start;
    color: var(--ink-light);
    font-size: 17px;
    line-height: 22px;
    white-space: nowrap;
  }
  .contact__icon {
    width: 16px;
    height: 16px;
    margin-right: 3px;
    margin-top: 3px;
    flex: none;
    fill: var(--brand-red);
  }
  .contact__row--address { top: 139px; }
  .contact__row--phone { top: 205px; }
  .contact__row--fax { top: 229px; }
  .contact__row--email { top: 252px; font-size: 16.5px; }
  .contact__row--web { top: 278px; font-size: 16.5px; }

  .tagline {
    position: absolute;
    left: 0; right: 0;
    top: 358px;
    text-align: center;
    color: var(--ink-light);
    font-size: 16.5px;
    letter-spacing: 0.2px;
  }
</style>
</head>
<body>

<section class="card card--front" aria-label="Business card front">
  <svg class="front-wedge" viewBox="0 0 708 406" aria-hidden="true">
    <polygon points="0,0 351,103 351,302 0,406" fill="var(--brand-red)"/>
  </svg>

  <div class="wordmark">
    <span class="wordmark__main">Norvane</span>
    <span class="wordmark__sub">Builders Limited</span>
  </div>

  <div class="contact">
    <p class="contact__company">Norvane Builders Limited</p>

    <div class="contact__row contact__row--address">
      <svg class="contact__icon" viewBox="0 0 16 16" aria-hidden="true">
        <path d="M8 0C4.7 0 2.4 2.5 2.4 5.6 2.4 9.6 8 16 8 16s5.6-6.4 5.6-10.4C13.6 2.5 11.3 0 8 0zm0 8.2a2.6 2.6 0 1 1 0-5.2 2.6 2.6 0 0 1 0 5.2z"/>
      </svg>
      <span>42 Brenton Street<br>Elk Harbour, NL, B3K 7T2</span>
    </div>

    <div class="contact__row contact__row--phone">
      <svg class="contact__icon" viewBox="0 0 16 16" aria-hidden="true">
        <path d="M3.6 1.2l2.3 2.6-1.2 2.1c.9 1.9 2.4 3.4 4.4 4.4l2.1-1.2 2.6 2.3-1.1 2.6C7.2 14.6 1.4 8.8 1 2.3z"/>
      </svg>
      <span>709-555-0147</span>
    </div>

    <div class="contact__row contact__row--fax">
      <svg class="contact__icon" viewBox="0 0 16 16" aria-hidden="true">
        <path d="M4 1h8v4H4zM1.5 6h13v6H12v3H4v-3H1.5zM5.5 10.5v3h5v-3z"/>
      </svg>
      <span>709-555-0192</span>
    </div>

    <div class="contact__row contact__row--email">
      <svg class="contact__icon" viewBox="0 0 16 16" aria-hidden="true">
        <path d="M1 3.5h14v9H1zM2.2 4.5L8 9l5.8-4.5v1.4L8 10.4 2.2 5.9z" fill-rule="evenodd"/>
      </svg>
      <span>info@norvanebuilders-example.com</span>
    </div>

    <div class="contact__row contact__row--web">
      <svg class="contact__icon" viewBox="0 0 16 16" aria-hidden="true">
        <circle cx="8" cy="8" r="6.5" fill="none" stroke="var(--brand-red)" stroke-width="1.3"/>
        <ellipse cx="8" cy="8" rx="2.8" ry="6.5" fill="none" stroke="var(--brand-red)" stroke-width="1.1"/>
        <path d="M1.5 8h13M2.5 4.8h11M2.5 11.2h11" stroke="var(--brand-red)" stroke-width="1.1"/>
      </svg>
      <span>www.norvanebuilders-example.com</span>
    </div>
  </div>
</section>

<section class="card card--back" aria-label="Business card back">
  <div class="wordmark">
    <span class="wordmark__main">Norvane</span>
    <span class="wordmark__sub">Builders Limited</span>
  </div>
  <p class="tagline">BUILT SOLID FROM EVERY FOUNDATION</p>
</section>

</body>
</html>
```